Marlo Pen Design Project

Two sided Flyer for marlo pen
see: www.marlo-pen.example
I have attached a copy with dimensions of last year's winner.
Replace Tobias Qualenbeck with Derek Holm

Use contact data from following web page link:
https://www.brindlewood.example/cgi/getHTML.cgi?page=/en_CA/fa/index.html&CIRN=418203

see uploaded photo file

Reason: Need more designs so am upgrading to guaranteed payout. i'll be submitting a colour picture of me soon.

fee is now guiaranteed with 15 day extension

```html
<!DOCTYPE html>
<html lang="en">
<head>
<meta charset="utf-8">
<title>Marlo Pen – Two Sided Flyer</title>
<link rel="stylesheet" href="https://fonts.googleapis.com/css2?family=Bodoni+Moda:wght@400&display=swap">
<style>
  :root {
    --navy: #2c6795;
    --stripe: #12a0d8;
    --orange: #f7953a;
    --ink: #111111;
    --paper: #ffffff;
    --light: #eef3f8;
  }
  html, body {
    margin: 0;
    padding: 0;
    width: 934px;
    height: 1200px;
    overflow: hidden;
    background: var(--paper);
  }
  .canvas {
    position: relative;
    width: 934px;
    height: 1200px;
    overflow: hidden;
  }

  /* Front side */
  .flyer-front {
    position: absolute;
    left: 18px;
    top: 27px;
    width: 544px;
    height: 704px;
    background: var(--navy);
    overflow: hidden;
  }
  .flyer-front__stripes {
    position: absolute;
    inset: 0;
    width: 100%;
    height: 100%;
  }
  .flyer-front__stripes polygon { fill: var(--stripe); }
  .flyer-front__title {
    position: absolute;
    left: 0;
    top: 250px;
    width: 100%;
    margin: 0;
    font-family: "Bodoni Moda", "Didot", serif;
    font-weight: 400;
    font-size: 92px;
    line-height: 1;
    color: var(--orange);
    text-align: center;
    white-space: nowrap;
  }

  /* Back side */
  .flyer-back {
    position: absolute;
    left: 516px;
    top: 731px;
    width: 313px;
    height: 406px;
    background: var(--navy);
    overflow: hidden;
  }
  .flyer-back__banner {
    position: absolute;
    left: 0;
    top: 0;
    width: 293px;
    height: 66px;
  }
  .flyer-back__banner polygon { fill: var(--orange); }
  .flyer-back__name {
    position: absolute;
    left: 8px;
    top: 5px;
    margin: 0;
    font-family: "Bodoni Moda", "Didot", serif;
    font-weight: 400;
    font-size: 38px;
    line-height: 1;
    color: var(--ink);
    letter-spacing: -0.5px;
    white-space: nowrap;
  }
  .flyer-back__role {
    position: absolute;
    left: 40px;
    top: 45px;
    margin: 0;
    font-family: "Bodoni Moda", "Didot", serif;
    font-size: 13px;
    line-height: 1;
    color: var(--ink);
    white-space: nowrap;
  }
  .flyer-back__contact {
    position: absolute;
    left: 0;
    top: 236px;
    width: 313px;
    margin: 0;
    font-family: "Bodoni Moda", "Didot", serif;
    font-style: normal;
    font-weight: 400;
    font-size: 24px;
    line-height: 1.2;
    color: var(--light);
    text-align: center;
    transform: rotate(-15deg);
    white-space: nowrap;
  }
</style>
</head>
<body>
<main class="canvas">

  <section class="flyer-front" aria-label="Flyer front">
    <svg class="flyer-front__stripes" viewBox="0 0 544 704" preserveAspectRatio="none" aria-hidden="true">
      <polygon points="0,440 544,265 544,285 0,462"/>
      <polygon points="0,486 544,311 544,331 0,507"/>
      <polygon points="0,531 544,356 544,375 0,551"/>
      <polygon points="0,576 544,401 544,419 0,594"/>
      <polygon points="0,621 544,446 544,463 0,638"/>
      <polygon points="0,665 544,491 544,507 0,681"/>
      <polygon points="60,704 544,556 544,569 100,704"/>
      <polygon points="196,704 544,608 544,618 232,704"/>
      <polygon points="344,704 544,656 544,663 374,704"/>
    </svg>
    <h1 class="flyer-front__title">Marlo Pen</h1>
  </section>

  <section class="flyer-back" aria-label="Flyer back">
    <svg class="flyer-back__banner" viewBox="0 0 293 66" aria-hidden="true">
      <polygon points="0,0 270,0 293,66 0,66"/>
    </svg>
    <h2 class="flyer-back__name">Derek Holm</h2>
    <p class="flyer-back__role">Brindlewood Financial Advisor</p>
    <address class="flyer-back__contact">
      (250) 555-0147<br>
      212 Larkspur Avenue East<br>
      Suite #204<br>
      Alder Bay,&nbsp; BC &nbsp; V0X 1K4
    </address>
  </section>

</main>
</body>
</html>
```